Fixing all glass products,fitting security doors,flyscreens,splashbacks,glazing

Looking for perhaps a liitle happy chap carrying a glass panel with crach throught it and maybe the pane of glass 'hurting' so it had 'pain'???
Open to suggestions

Security

Brightway Glazeworks
Dale Morrow
Specialising in security doors,flyscreens,splashbacks
0451736208
dalemorrow418@postvane.com

```html
<!DOCTYPE html>
<html lang="en">
<head>
<meta charset="utf-8">
<title>Brightway Glazeworks – Business Card</title>
<link rel="stylesheet" href="https://fonts.googleapis.com/css2?family=PT+Sans:wght@400;700&display=swap">
<style>
  :root {
    --backdrop: #4b4b4d;
    --backdrop-dark: #2e2e30;
    --card-white: #ffffff;
    --card-mist: #e6e7e9;
    --title-blue: #1b70b7;
    --band-dark: #3b3b3d;
    --wave-bright: #00aee9;
    --wave-deep: #2346a0;
    --contact-white: #ffffff;
  }
  html, body {
    margin: 0;
    padding: 0;
    width: 1200px;
    height: 999px;
    overflow: hidden;
  }
  body {
    position: relative;
    background: radial-gradient(ellipse at center, var(--backdrop) 40%, var(--backdrop-dark) 100%);
    font-family: "PT Sans", Tahoma, sans-serif;
  }
  .business-card {
    position: absolute;
    left: 68px;
    top: 192px;
    width: 1064px;
    height: 614px;
    background: linear-gradient(to bottom, var(--card-mist) 0px, var(--card-white) 120px);
    overflow: hidden;
  }
  .card-wave {
    position: absolute;
    left: 0;
    top: 0;
    width: 1064px;
    height: 614px;
  }
  .card-heading {
    position: absolute;
    left: 0;
    right: 0;
    top: 86px;
    margin: 0;
    text-align: center;
    color: var(--title-blue);
    font-weight: 400;
    font-size: 72px;
    line-height: 92px;
    letter-spacing: 1px;
  }
  .card-heading span { display: block; }
  .specialties {
    position: absolute;
    left: 42px;
    top: 460px;
    margin: 0;
    color: var(--contact-white);
    font-size: 28px;
    line-height: 37px;
  }
  .specialties strong { font-weight: 700; display: block; }
  .contact-list {
    position: absolute;
    left: 582px;
    top: 476px;
    margin: 0;
    padding: 0;
    list-style: none;
    color: var(--contact-white);
    font-size: 30px;
    line-height: 47px;
  }
  .contact-list li {
    display: flex;
    align-items: center;
    gap: 18px;
  }
  .contact-icon { width: 26px; height: 26px; flex: none; }
</style>
</head>
<body>
  <div class="business-card">
    <svg class="card-wave" viewBox="0 0 1064 614" aria-hidden="true">
      <defs>
        <radialGradient id="waveGlow" cx="532" cy="545" r="560" gradientUnits="userSpaceOnUse" gradientTransform="translate(532 545) scale(1 0.35) translate(-532 -545)">
          <stop offset="0" stop-color="var(--wave-bright)"/>
          <stop offset="0.45" stop-color="#1f9ad8"/>
          <stop offset="1" stop-color="var(--wave-deep)"/>
        </radialGradient>
      </defs>
      <path d="M0 430 Q532 335 1064 436 L1064 443 Q532 344 0 439 Z" fill="var(--band-dark)"/>
      <path d="M0 438 Q532 344 1064 442 L1064 614 L0 614 Z" fill="url(#waveGlow)"/>
    </svg>

    <h1 class="card-heading">
      <span class="company-name">Brightway Glazeworks</span>
      <span class="person-name">Dale Morrow</span>
    </h1>

    <p class="specialties">
      <strong>Specialising in</strong>
      security doors, flyscreens<br>
      splashbacks
    </p>

    <ul class="contact-list">
      <li>
        <svg class="contact-icon" viewBox="0 0 24 24" aria-label="Phone">
          <path fill="#fff" d="M6.6 2.5c.6-.3 1.3-.1 1.6.5l1.6 3.2c.3.6.1 1.2-.4 1.6L8 8.8c.9 2.3 2.9 4.3 5.2 5.2l1-1.4c.4-.5 1-.7 1.6-.4l3.2 1.6c.6.3.8 1 .5 1.6l-1 2c-.4.8-1.3 1.2-2.2 1C9.8 17.2 5.8 13.2 4.6 7.7c-.2-.9.2-1.8 1-2.2z"/>
          <path fill="none" stroke="#fff" stroke-width="1.6" stroke-linecap="round" d="M14 4.5a5.5 5.5 0 0 1 5.5 5.5M14 1.5a8.5 8.5 0 0 1 8.5 8.5"/>
        </svg>
        <span>0451736208</span>
      </li>
      <li>
        <svg class="contact-icon" viewBox="0 0 24 24" aria-label="Email">
          <path fill="#fff" d="M2 10 L12 3 L22 10 V21 H2 Z"/>
          <path fill="none" stroke="var(--wave-deep)" stroke-width="1.6" d="M2.5 10.5 L12 17 L21.5 10.5"/>
          <circle cx="12" cy="11" r="2.2" fill="var(--wave-deep)"/>
        </svg>
        <span>dalemorrow418@postvane.com</span>
      </li>
    </ul>
  </div>
</body>
</html>
```